Customizable Gift Note Card Design

I need a gift note card designed for my Healthy Snacks Care Package company. I need to be able to customize each card with the customer's gift message to the recipient and print to a standard printer.

The card should be single-sided 5 x 7, include our logo, keep colors and graphics simple since they will be printed for each individual order on a standard printer. I would like the following quote to be included in a small and subtle way: "Food is symbolic of love when words are inadequate." —Bertram K. Osslund. Our website thebrightpantrybites.example should also be included.

I have included pictures of our product packaging for reference.

Target Market(s)

Gift recipients: Students, people recovering from illness, housewarming, thank you gifts...etc.

Industry/Entity Type

It Company

Colors

Designer to choose colors to be used in the design.

Requirements
Must have
• We are looking for a simple, cute and elegant gift card that reflects our branding. Must be customizable and printable on a standard printer.
• Must be single-sided 5x7.

```html
<!DOCTYPE html>
<html lang="en">
<head>
<meta charset="utf-8">
<title>The Bright Pantry – Gift Card</title>
<link rel="stylesheet" href="https://fonts.googleapis.com/css2?family=Comfortaa:wght@400;700&display=swap">
<style>
  :root {
    --backdrop: #2a2a2a;
    --card-red: #c3141f;
    --card-red-deep: #7a0a10;
    --strip-white: #ffffff;
    --ink: #111111;
    --text-light: #ffffff;
    --quote-pink: #f3c9cb;
    --dash: rgba(255, 255, 255, 0.55);
  }
  * { margin: 0; padding: 0; box-sizing: border-box; }
  html, body {
    width: 1200px;
    height: 900px;
    overflow: hidden;
    background: var(--backdrop);
    font-family: "Comfortaa", sans-serif;
  }
  .gift-card {
    position: absolute;
    left: 100px;
    top: 93px;
    width: 1000px;
    height: 714px;
    border-radius: 36px;
    overflow: hidden;
    background: radial-gradient(ellipse at 55% 45%, var(--card-red) 0%, #a70f18 45%, var(--card-red-deep) 100%);
  }
  .brand-strip {
    position: absolute;
    left: 0;
    top: 0;
    width: 200px;
    height: 100%;
    background: var(--strip-white);
    border-radius: 36px 80px 80px 36px / 36px 160px 160px 36px;
  }
  .brand-dot {
    position: absolute;
    left: 102px;
    top: 80px;
    width: 36px;
    height: 36px;
    border-radius: 50%;
    background: var(--card-red);
  }
  .brand-name {
    position: absolute;
    left: 120px;
    top: 330px;
    transform: translate(-50%, -50%) rotate(-90deg);
    white-space: nowrap;
    font-size: 34px;
    font-weight: 700;
    color: var(--ink);
  }
  .website {
    position: absolute;
    left: 50px;
    top: 440px;
    transform: translate(-50%, -50%) rotate(-90deg);
    white-space: nowrap;
    font-size: 20px;
    font-weight: 700;
    color: var(--ink);
  }
  .dash-frame {
    position: absolute;
    inset: 0;
    pointer-events: none;
  }
  .card-heading {
    position: absolute;
    right: 70px;
    top: 86px;
    display: flex;
    align-items: center;
    gap: 18px;
    color: var(--text-light);
  }
  .card-heading .heading-brand {
    font-size: 28px;
    font-weight: 700;
  }
  .card-heading .divider {
    width: 2px;
    height: 44px;
    background: var(--text-light);
  }
  .card-heading .heading-label {
    font-size: 32px;
    font-weight: 400;
    letter-spacing: 1px;
  }
  .gift-message {
    position: absolute;
    left: 300px;
    top: 235px;
    width: 570px;
    font-size: 30px;
    line-height: 1.42;
    color: var(--text-light);
  }
  .gift-quote {
    position: absolute;
    right: 240px;
    top: 520px;
    text-align: right;
    font-size: 16px;
    line-height: 1.5;
    color: var(--quote-pink);
  }
  .gift-quote cite {
    display: block;
    font-style: normal;
    color: var(--text-light);
  }
  .value-badge {
    position: absolute;
    right: 40px;
    top: 482px;
    width: 150px;
    height: 150px;
    border-radius: 50%;
    background: var(--strip-white);
    display: flex;
    align-items: center;
    justify-content: center;
  }
  .value-badge::before {
    content: "";
    position: absolute;
    inset: 12px;
    border-radius: 50%;
    border: 2px dashed var(--card-red);
  }
  .value-badge .amount {
    font-size: 42px;
    font-weight: 700;
    color: var(--card-red);
  }
</style>
</head>
<body>
  <main class="gift-card">
    <svg class="dash-frame" width="1000" height="714" viewBox="0 0 1000 714" aria-hidden="true">
      <path d="M210 66 H950 V490" fill="none" stroke="var(--dash)" stroke-width="2" stroke-dasharray="12 10"/>
    </svg>

    <aside class="brand-strip">
      <span class="brand-dot"></span>
      <span class="brand-name">The Bright Pantry</span>
      <span class="website">thebrightpantrybites.example</span>
    </aside>

    <header class="card-heading">
      <span class="heading-brand">The Bright Pantry</span>
      <span class="divider"></span>
      <span class="heading-label">GIFT CARD</span>
    </header>

    <p class="gift-message">Lorem ipsum dolor sit amet, consectetuer adipiscing elit. Ulioson commodo ligula eget dolor. Aenean massa.</p>

    <blockquote class="gift-quote">
      “Food is symbolic of love when<br>words are inadequate.”
      <cite>Bertram K. Osslund</cite>
    </blockquote>

    <div class="value-badge"><span class="amount">$100</span></div>
  </main>
</body>
</html>
```